Modern Informational OBGYN website

Looking for a modern Wordpress website for a general OBGYN practice in Florida with a specialty in High Risk Obstetrics. We had an old Joomla website that crashed and we lost most of the files. It was over 10 years old and needed a refresh anyway.

Our practice serves a multicultural patient population (white, black, Spanish and Indian) and we would like our website to reflect that diversity. Our company colors are sunshine yellow (#ECBF6D) often combined with black, white and steel blue (#7191BE) in the "life" part of our logo (attached) depending on the background. Our tagline is "We're specialist in You!" Overall the site should have a clean modern yet comfortable feel. One that portrays friendliness and competence. At least 6 pages (Home, Obstetrics, Gynecology, News, Patient Education and Resources). Rotating stock pictures or videos are fine for the headers of the pages if the design you're considering calls for it. Interesting and creative use of typography and icons are encouraged.

The home page should have a call to action to schedule an appointment as well as a link to our patient portal. Other than the home and news pages, the other pages should have a similar look and feel. The home page should have sections on "About Us", "Medical Staff" (with pictures and brief bio for 2 male doctors, 2 female midwives and 1 female nurse practitioner), "Services" and "Location". The news page will be a closed blog that will not allow comments or responses. Both the obstetrics and the gynecology pages will have an educational blurb on the respective topics followed by a list of our services for each topic. Would be nice on the obstetrics page to have information and graphics changes that occur during each trimester (but not necessary). The resource page will have sections on at least "Office Forms", Office Policies", "OB Guide" each with multiple downloadable PDF's. Also a section on "Insurance" with a list of all the major insurance plans that we take with links to their company websites. The address, link and map to our hospital and their website can also go on this page. The Patient Education Page can be broken into 3 sections Obstetrics, Gynecology which both will have definition of medical disorders followed by FAQ's and "Helpful Links" which would have links to other website for medical information.

That's all that I can think of right now. The above is to help guide you but I am flexible, if the website design dictates a better flow of information. Looking forward to seeing what you can come up with. Down the road, I will be looking to the winning designer to produce matching brochures, full, half and quarter page media ads to have on hand for the practices further needs.

Target Market(s)

Women looking medical services

Industry/Entity Type

Medical

Coding

Coded - Design and coding required

Number of Pages Required

5+ page

Font styles to use
Sans Serif
Script

Colors

Designer to choose colors to be used in the design.

Requirements
Must have
• None. See projects description for suggestions
Nice to have
• infographics like information on stages of pregnancy on the obstetrics page

```html
<!DOCTYPE html>
<html lang="en">
<head>
<meta charset="utf-8">
<title>Brightwell OB/GYN</title>
<link href="https://fonts.googleapis.com/css2?family=Montserrat:wght@400;500;600;700&family=Lora:wght@400&display=swap" rel="stylesheet">
<style>
:root{
  --gold:#f1bd4b;
  --gold-dark:#d9a437;
  --steel:#56749b;
  --steel-light:#7f9cc0;
  --ink:#1f1f1f;
  --text:#3a3a3a;
  --muted:#666;
  --pale:#f1f5f9;
  --white:#fff;
  --line:#d7d7d7;
}
*{margin:0;padding:0;box-sizing:border-box}
html,body{width:1200px;height:3342px;overflow:hidden}
body{position:relative;font-family:'Montserrat',sans-serif;color:var(--text);background:var(--white)}
.abs{position:absolute}
.btn{position:absolute;display:flex;align-items:center;justify-content:center;background:var(--gold);color:var(--ink);font-size:11px;font-weight:500;box-shadow:0 2px 0 var(--gold-dark);border-radius:2px;white-space:nowrap}
.btn.big{font-size:12px}
/* header */
.site-header{top:0;left:0;width:1200px;height:74px;background:var(--white);box-shadow:0 1px 6px rgba(0,0,0,.08);z-index:5}
.brand{position:absolute;display:flex;align-items:center;gap:6px;font-weight:700;color:var(--steel)}
.brand .dot{width:14px;height:14px;border-radius:50%;background:var(--gold)}
.main-nav{position:absolute;left:365px;top:30px;display:flex;gap:26px;font-size:11px;font-weight:600;color:#333}
.call{position:absolute;left:798px;top:18px;display:flex;gap:10px;align-items:center}
.call .ico{width:32px;height:32px;border-radius:50%;background:var(--steel);display:flex;align-items:center;justify-content:center}
.call small{display:block;font-size:10px;color:#333}
.call strong{font-size:19px;color:var(--gold);font-weight:600}
/* hero */
.hero{top:74px;left:0;width:1200px;height:620px;background:linear-gradient(180deg,#c8d6e3 0%,#e7eadc 55%,#f8f7d4 100%)}
.hero h1{position:absolute;left:162px;top:132px;font-size:67px;line-height:68px;font-weight:700;color:var(--steel)}
.hero-photo{position:absolute;left:790px;top:22px;width:225px;height:450px;background:linear-gradient(180deg,#6b5a52 0%,#3a3f6b 40%,#2f3563 100%);border-radius:110px 110px 0 0;opacity:.85}
.dots{position:absolute;left:162px;top:464px;display:flex;gap:6px}
.dots span{width:10px;height:10px;border-radius:50%;border:1.5px solid var(--steel)}
.dots span.on{background:var(--gold);border-color:var(--gold)}
/* about */
.eyebrow{font-size:13px;font-weight:600;letter-spacing:3px;color:var(--steel)}
.about-head{top:724px;left:0;width:1200px;text-align:center;font-size:29px;line-height:37px;font-weight:400;color:var(--ink)}
.about-head .accent{color:var(--steel);font-weight:600}
.about-head b{font-weight:700}
.about-lead{top:810px;left:250px;width:700px;text-align:center;font-size:14.5px;line-height:27px;color:#222}
.about-photo{left:161px;top:934px;width:412px;height:321px;background:linear-gradient(120deg,#e8edf2 0%,#b9d6ea 45%,#f2f2f2 100%)}
.about-text{left:638px;top:930px;width:412px;font-size:11.5px;line-height:26px;color:#444}
/* staff */
.staff-bg{top:1400px;left:0;width:1200px;height:792px;background:var(--pale)}
.staff-title{left:163px;top:1508px;font-size:29px;font-weight:700;color:var(--ink)}
.staff-text{left:162px;top:1572px;width:495px;font-size:11px;line-height:23.5px;color:#444}
.staff-text p+p{margin-top:16px}
.round-arrow{width:46px;height:46px;border-radius:50%;background:#8796a8;display:flex;align-items:center;justify-content:center}
.doc-photo{left:700px;top:1446px;width:364px;height:542px;background:linear-gradient(180deg,#f1f5f9 0%,#e6e9ee 30%,#d9dee6 100%);border-radius:160px 160px 0 0}
.thumbs{left:161px;top:1988px;width:877px;height:162px;display:flex;box-shadow:0 4px 12px rgba(0,0,0,.12);background:var(--white)}
.thumbs div{flex:1;background:#eef0f2}
.thumbs div.on{background:linear-gradient(180deg,#c9ccd3,#e8e9ec)}
/* services */
.svc-nav{top:2278px;left:1000px;display:flex;gap:6px}
.svc-nav span{width:24px;height:24px;border:1px solid #ccc;display:flex;align-items:center;justify-content:center;background:#fafafa}
.card{position:absolute;top:2335px;width:213px;height:268px;border:1px solid #cfcfcf;background:var(--white)}
.card .icon{position:absolute;left:20px;top:50px}
.card .bar{position:absolute;left:20px;top:100px;width:30px;height:2px;background:var(--gold)}
.card h3{position:absolute;left:20px;top:112px;font-size:18px;font-weight:400;color:#333;white-space:nowrap}
.card p{position:absolute;left:20px;top:148px;width:180px;font-size:11.5px;line-height:22px;color:#555}
.card .more{position:absolute;left:20px;top:226px;font-size:11.5px;color:var(--steel);display:flex;align-items:center;gap:6px;white-space:nowrap}
/* footer */
.footer{top:2770px;left:0;width:1200px;height:572px;background:linear-gradient(160deg,#8aa5c7 0%,#7694bb 55%,#6483ab 100%)}
.silhouette{position:absolute;left:940px;top:110px;width:240px;height:462px;border-radius:120px 120px 0 0;background:rgba(70,100,140,.25)}
.map{left:161px;top:2853px;width:342px;height:305px;background:linear-gradient(135deg,#eef0f2 0%,#e3e7ea 100%);border:1px solid #ccd}
.contact-title{left:568px;top:2902px;font-size:36px;font-weight:400;color:var(--white);letter-spacing:.5px}
.contact-list{left:570px;top:2968px;color:var(--white);font-size:13px;line-height:24px}
.contact-list li{list-style:none;display:flex;gap:16px;margin-bottom:6px}
.contact-list svg{flex:none;margin-top:5px}
.quick-title{left:163px;top:3210px;font-family:'Lora',serif;font-weight:400;font-size:16px;color:var(--white);letter-spacing:.5px}
.quick-links{left:163px;top:3245px;display:grid;grid-template-columns:81px 79px 60px;row-gap:10px;font-size:13px;color:var(--white)}
.foot-brand{left:546px;top:3232px;font-size:22px;color:var(--white)}
.copy{left:546px;top:3270px;font-size:12.5px;color:var(--white)}
</style>
</head>
<body>

<header class="abs site-header">
  <div class="brand" style="left:32px;top:22px;font-size:22px"><span class="dot"></span>Brightwell</div>
  <nav class="main-nav"><span>HOME</span><span>ABOUT</span><span>SERVICES</span><span>OUR STAFF</span><span>BLOG</span><span>CONTACT</span></nav>
  <div class="call">
    <span class="ico"><svg width="14" height="14" viewBox="0 0 24 24" fill="none" stroke="#fff" stroke-width="2"><path d="M5 3h4l2 5-3 2a11 11 0 0 0 6 6l2-3 5 2v4a2 2 0 0 1-2 2A18 18 0 0 1 3 5a2 2 0 0 1 2-2z"/></svg></span>
    <div><small>Call Us Today!</small><strong>555-210-4870</strong></div>
  </div>
  <span class="btn" style="left:1001px;top:16px;width:175px;height:40px">Schedule An Appoinment</span>
</header>

<section class="abs hero">
  <h1>We’re Specialist<br>in You!</h1>
  <span class="btn" style="left:161px;top:294px;width:176px;height:41px">Schedule An Appoinment</span>
  <span class="btn" style="left:357px;top:294px;width:146px;height:41px">Our Patient Portal</span>
  <div class="dots"><span class="on"></span><span></span><span></span><span></span></div>
  <div class="hero-photo" role="img" aria-label="Photo of a pregnant woman in a navy dress, side view"></div>
</section>
<svg class="abs" style="left:0;top:530px" width="1200" height="186" viewBox="0 0 1200 186" preserveAspectRatio="none">
  <defs>
    <linearGradient id="heroBlue" x1="0" x2="1"><stop offset="0" stop-color="#5c7aa1"/><stop offset=".5" stop-color="#8aa7c8"/><stop offset="1" stop-color="#5a789f"/></linearGradient>
    <linearGradient id="heroGrey" x1="0" x2="1"><stop offset="0" stop-color="#e5e5e5"/><stop offset="1" stop-color="#9a9a9a"/></linearGradient>
  </defs>
  <path d="M0 65 C300 150 600 110 880 30 C1000 0 1100 -5 1200 10 V186 H0Z" fill="url(#heroBlue)"/>
  <path d="M0 140 C250 160 550 140 800 80 C950 40 1100 55 1200 115 V186 H0Z" fill="#fff"/>
  <path d="M690 100 C900 40 1110 50 1200 150 V178 C1100 90 900 75 690 100Z" fill="url(#heroGrey)"/>
</svg>

<div class="abs eyebrow" style="top:692px;left:0;width:1200px;text-align:center">About Us</div>
<h2 class="abs about-head">Lorem Ipsum Dolor <span class="accent">Consectetuer...</span><br>Adipiscing&nbsp; <b>Elit, Sed Diam .</b></h2>
<p class="abs about-lead">Lorem ipsum dolor sit amet, consectetuer adipiscing elit, sed diam nonummy nibh euismod tincidunt ut laoreet dolore magna aliquam erat volutpat. Ut wisi enim ad minim veniam, quis nostrud exerci tation ullamcorper suscipit lobortis nisl ut aliquip ex ea commodo</p>
<div class="abs about-photo" role="img" aria-label="Photo of a pregnant patient talking with a doctor holding a clipboard"></div>
<p class="abs about-text">Lorem ipsum dolor sit amet, consectetuer adipiscing elit, sed diam nonummy nibh euismod tincidunt ut laoreet dolore magna aliquam erat volutpat. Ut wisi enim ad minim veniam, quis nostrud exerci tation ullamcorper suscipit lobortis nisl ut aliquip ex ea commodo consequat. Duis autem vel eum iriure dolor in hendrerit in vulputate velit esse molestie consequat, vel illum dolore eu feugiat nulla facilisis at vero eros et accumsan et iusto odio dignissim qui blandit praesent luptatum zzril delenit augue duis dolore te feugait nulla facilisi.</p>
<span class="btn big" style="left:636px;top:1204px;width:214px;height:49px">READ MORE ABOUT BRIGHTWELL</span>

<div class="abs staff-bg"></div>
<svg class="abs" style="left:0;top:1330px" width="1200" height="120" viewBox="0 0 1200 120" preserveAspectRatio="none">
  <path d="M0 110 C300 60 700 -10 1200 40 V120 H0Z" fill="#f1f5f9"/>
  <path d="M0 0 C80 60 250 90 460 50 C250 105 60 85 0 45Z" fill="#5b799f"/>
</svg>
<div class="abs eyebrow" style="left:163px;top:1482px">Our Medical Staff</div>
<h2 class="abs staff-title">About Dr. Martin Hale</h2>
<div class="abs staff-text">
  <p>Lorem ipsum dolor sit amet, consectetuer adipiscing elit, sed diam nonummy nibh euismod tincidunt ut laoreet dolore magna aliquam erat volutpat. Ut wisi enim ad minim veniam, quis nostrud exerci tation ullamcorper suscipit lobortis nisl ut aliquip ex ea commodo consequat. Duis autem vel eum iriure dolor in</p>
  <p>Lorem ipsum dolor sit amet, consectetuer adipiscing elit, sed diam nonummy nibh euismod tincidunt ut laoreet dolore magna aliquam erat volutpat. Ut wisi enim ad minim veniam, quis nostrud exerci tation ullamcorper suscipit lobortis nisl ut aliquip ex ea commodo consequat. Duis autem vel eum iriure dolor in hendrerit in vulputate velit esse molestie consequat, vel illum dolore eu feugiat nulla facilisis at vero eros et accumsan et iusto odio dignissim qui blandit praesent luptatum</p>
</div>
<span class="btn big" style="left:161px;top:1865px;width:214px;height:49px">MORE ABOUT DR. HALE</span>
<span class="abs round-arrow" style="left:72px;top:1692px"><svg width="20" height="14" viewBox="0 0 20 14" fill="none" stroke="#fff" stroke-width="2"><path d="M19 7H2M8 1 2 7l6 6"/></svg></span>
<span class="abs round-arrow" style="left:1107px;top:1692px"><svg width="20" height="14" viewBox="0 0 20 14" fill="none" stroke="#fff" stroke-width="2"><path d="M1 7h17M12 1l6 6-6 6"/></svg></span>
<div class="abs doc-photo" role="img" aria-label="Portrait of a smiling male doctor in a white coat with arms crossed"></div>
<div class="abs thumbs" role="img" aria-label="Row of five staff portrait thumbnails">
  <div class="on"></div><div></div><div></div><div></div><div></div>
</div>

<div class="abs eyebrow" style="left:163px;top:2281px">Our Services</div>
<div class="abs svc-nav">
  <span><svg width="8" height="12" viewBox="0 0 8 12" fill="none" stroke="#333" stroke-width="1.5"><path d="M7 1 2 6l5 5"/></svg></span>
  <span><svg width="8" height="12" viewBox="0 0 8 12" fill="none" stroke="#333" stroke-width="1.5"><path d="m1 1 5 5-5 5"/></svg></span>
</div>

<article class="card" style="left:157px">
  <svg class="icon" width="40" height="36" viewBox="0 0 40 36" fill="none" stroke="#d9a437" stroke-width="1.6"><path d="M4 6c4 0 6 4 10 6v8c0 6 4 10 6 10s6-4 6-10v-8c4-2 6-6 10-6"/><path d="M20 30v5"/></svg>
  <span class="bar"></span><h3>Gynaecology</h3>
  <p>Lorem ipsum dolor sit amet, consectetuer adipiscing elit, Lorem ipsum dolor.....</p>
  <span class="more">LEARN MORE <svg width="44" height="8" viewBox="0 0 44 8" fill="none" stroke="#aab" stroke-width="1"><path d="M0 4h42M38 1l4 3-4 3"/></svg></span>
</article>
<article class="card" style="left:387px">
  <svg class="icon" width="40" height="40" viewBox="0 0 40 40" fill="none" stroke="#d9a437" stroke-width="1.6"><circle cx="20" cy="22" r="15"/><circle cx="20" cy="18" r="5"/><path d="M6 26c6 2 10 6 14 6s8-4 14-6"/></svg>
  <span class="bar"></span><h3>Obstetrical Care</h3>
  <p>Lorem ipsum dolor sit amet, consectetuer adipiscing elit, Lorem ipsum dolor.....</p>
  <span class="more">LEARN MORE <svg width="44" height="8" viewBox="0 0 44 8" fill="none" stroke="#aab" stroke-width="1"><path d="M0 4h42M38 1l4 3-4 3"/></svg></span>
</article>
<article class="card" style="left:616px">
  <svg class="icon" width="30" height="52" viewBox="0 0 30 52" fill="none" stroke="#d9a437" stroke-width="1.6" style="top:38px"><circle cx="12" cy="7" r="5"/><path d="M10 14c-4 8 -2 14 6 18c8 4 6 12 -4 18"/></svg>
  <span class="bar"></span><h3>Antenatal Care</h3>
  <p>Lorem ipsum dolor sit amet, consectetuer adipiscing elit, Lorem ipsum dolor.....</p>
  <span class="more">LEARN MORE <svg width="44" height="8" viewBox="0 0 44 8" fill="none" stroke="#aab" stroke-width="1"><path d="M0 4h42M38 1l4 3-4 3"/></svg></span>
</article>
<article class="card" style="left:844px">
  <svg class="icon" width="40" height="40" viewBox="0 0 40 40" fill="none" stroke="#d9a437" stroke-width="1.6"><path d="M4 16a12 10 0 1 1 6 9l-6 3 2-6"/><circle cx="26" cy="26" r="10"/><path d="M26 30l-4-4a2 2 0 0 1 4-2 2 2 0 0 1 4 2z"/></svg>
  <span class="bar"></span><h3>Biofeedback</h3>
  <p>Lorem ipsum dolor sit amet, consectetuer adipiscing elit, Lorem ipsum dolor.....</p>
  <span class="more">LEARN MORE <svg width="44" height="8" viewBox="0 0 44 8" fill="none" stroke="#aab" stroke-width="1"><path d="M0 4h42M38 1l4 3-4 3"/></svg></span>
</article>

<footer class="abs footer">
  <div class="silhouette" role="img" aria-label="Faint silhouette of a pregnant woman"></div>
</footer>
<svg class="abs" style="left:0;top:2660px" width="1200" height="140" viewBox="0 0 1200 140" preserveAspectRatio="none">
  <defs>
    <linearGradient id="footGrey" x1="0" x2="1"><stop offset="0" stop-color="#9c9c9c"/><stop offset="1" stop-color="#e6e6e6"/></linearGradient>
    <linearGradient id="footBlue" x1="0" x2="1"><stop offset="0" stop-color="#8aa5c7"/><stop offset="1" stop-color="#5b799f"/></linearGradient>
  </defs>
  <path d="M0 130 C400 140 700 80 1000 20 C1100 0 1150 0 1200 10 V140 H0Z" fill="url(#footBlue)"/>
  <path d="M0 128 C400 138 700 82 1000 35 C1100 18 1160 30 1200 60 V140 H0Z" fill="#8aa5c7" opacity=".6"/>
  <path d="M0 20 C200 80 400 85 560 60 C400 110 150 100 0 62Z" fill="url(#footGrey)"/>
  <path d="M720 80 C900 20 1100 15 1200 60 C1100 35 900 45 720 80Z" fill="#fff"/>
</svg>
<div class="abs map" role="img" aria-label="Street map showing the office location"></div>
<h2 class="abs contact-title">CONTACT INFO</h2>
<ul class="abs contact-list">
  <li><svg width="14" height="16" viewBox="0 0 14 16" fill="#fff"><path d="M7 0a5 5 0 0 1 5 5c0 4-5 8-5 8S2 9 2 5a5 5 0 0 1 5-5zm0 3a2 2 0 1 0 0 4 2 2 0 0 0 0-4z"/></svg><span>2280 Harbor Palm Avenue, Suite<br>210, Coral Grove, FL 33000</span></li>
  <li><svg width="14" height="14" viewBox="0 0 24 24" fill="#fff"><path d="M5 2h4l2 5-3 2a11 11 0 0 0 6 6l2-3 5 2v4a2 2 0 0 1-2 2A18 18 0 0 1 3 4a2 2 0 0 1 2-2z"/></svg><strong style="font-weight:600">555-210-4870</strong></li>
  <li><svg width="14" height="14" viewBox="0 0 14 14" fill="#fff"><rect x="3" y="0" width="8" height="4"/><rect x="0" y="5" width="14" height="6" rx="1"/><rect x="3" y="9" width="8" height="5"/></svg><span>555-210-4871</span></li>
  <li><svg width="16" height="12" viewBox="0 0 16 12" fill="#fff"><path d="M0 0h16v12H0z"/><path d="M0 0l8 6 8-6" stroke="#7694bb" fill="none"/></svg><span>hello@brightwellobgyn.com</span></li>
</ul>
<h4 class="abs quick-title">QUICK LINKS</h4>
<nav class="abs quick-links"><span>Home</span><span>About Us</span><span>Services</span><span>Our Staff</span><span>Blog</span><span>Contact</span></nav>
<div class="brand foot-brand"><span class="dot"></span>Brightwell</div>
<div class="abs copy">© 2022 Brightwellobgyn.</div>

</body>
</html>
```